Local Electrical company need some kick ass business cards

In need of some in your face design business cards for a family owned electrical service company in Edmonton, Alberta Canada. We provide reliable and trustworthy electrical service for commercial and residential work in the Edmonton and area. We have been in business for 25 years.

Target Market(s)

Residential and commercial electrical

Industry/Entity Type

Business

Contact Information for Business Card

Your welcome to change and modify the Vantor Wiring logo. please include the lightbulb! Our Colours are black and green please stay with that.
Please include a name phone number and address on the card
phone number - 780-555-0138
#22, 418 Maple Ridge Rd, St.Albert, Alberta.
Two things that need to be on the card.
"your friendly neighborhood electrictrician"
Commercial & residential electrical repair and service

Colors
9bcb3c

Requirements
Must have
• Light bulb guy Attached
• "your friendly neighborhood electrictrician"
• Commercial & residential electrical repair and service
• phone number - 780-555-0138
• #22, 418 Maple Ridge Rd, St.Albert, Alberta.
• Our colours are black and green
Nice to have
• go wild i want something loud

```html
<!DOCTYPE html>
<html lang="en">
<head>
<meta charset="utf-8">
<title>Vantor Wiring – Business Card</title>
<link href="https://fonts.googleapis.com/css2?family=Lato:wght@400;700;900&family=Russo+One&display=swap" rel="stylesheet">
<style>
  :root {
    --green: #9bcb3c;
    --green-bright: #8fd400;
    --black: #0b0b0b;
    --white: #ffffff;
    --ink: #1d1d1d;
    --stage: #3a3430;
    --bulb-light: #dff3f6;
  }
  * { box-sizing: border-box; margin: 0; padding: 0; }
  html, body {
    width: 1200px; height: 935px; overflow: hidden;
    background: var(--stage);
    font-family: "Lato", Arial, sans-serif;
  }
  .canvas { position: relative; width: 1200px; height: 935px; }
  .card {
    position: absolute; top: 170px;
    width: 340px; height: 595px;
    border-radius: 26px; overflow: hidden;
    box-shadow: 0 18px 40px rgba(0,0,0,.45);
  }
  /* back side */
  .card-back { left: 200px; background: var(--black); }
  .back-brand {
    position: absolute; top: 230px; left: 0; right: 0;
    display: flex; align-items: center; justify-content: center; gap: 12px;
  }
  .brand-dot { width: 18px; height: 18px; border-radius: 50%; background: var(--green-bright); flex: none; }
  .back-brand .brand-name { color: var(--green-bright); font-weight: 900; font-size: 32px; letter-spacing: .5px; }
  .tagline {
    position: absolute; top: 300px; left: 0; right: 0; text-align: center;
    color: var(--green-bright); font-size: 14px; letter-spacing: .3px;
  }
  /* front side */
  .card-front { left: 660px; background: var(--white); }
  .front-brand {
    position: absolute; top: 52px; left: 26px;
    display: flex; align-items: center; gap: 10px;
  }
  .front-brand .brand-name { color: var(--black); font-weight: 900; font-size: 26px; }
  .mascot {
    position: absolute; top: 130px; left: 168px;
    width: 160px; height: 250px; border-radius: 80px 80px 40px 40px;
    background: linear-gradient(160deg, var(--green-bright) 0%, var(--bulb-light) 45%, #b9c4c6 100%);
  }
  .person { position: absolute; top: 400px; left: 26px; }
  .person-name { font-family: "Russo One", sans-serif; color: var(--green-bright); font-size: 20px; letter-spacing: 1px; }
  .person-role { color: var(--ink); font-size: 13px; margin-top: 4px; padding-left: 16px; }
  .contact { position: absolute; top: 458px; left: 26px; right: 16px; color: var(--ink); font-size: 12px; }
  .contact .address { margin-bottom: 8px; padding-left: 16px; }
  .contact-row { display: flex; align-items: center; gap: 12px; padding-left: 44px; margin-top: 5px; font-size: 13px; }
  .contact-row svg { width: 14px; height: 14px; flex: none; }
  .service-band {
    position: absolute; left: 0; right: 0; bottom: 0; height: 62px;
    background: var(--green-bright); border-top: 6px solid var(--black);
    border-radius: 34px 0 0 0;
    display: flex; align-items: center; justify-content: center;
    color: var(--ink); font-size: 11.5px; font-weight: 700;
  }
</style>
</head>
<body>
<main class="canvas">
  <section class="card card-back" aria-label="Card back">
    <div class="back-brand">
      <span class="brand-dot"></span>
      <span class="brand-name">Vantor Wiring</span>
    </div>
    <p class="tagline">your friendly neighborhood electrictrician</p>
  </section>

  <section class="card card-front" aria-label="Card front">
    <div class="front-brand">
      <span class="brand-dot"></span>
      <span class="brand-name">Vantor Wiring</span>
    </div>
    <div class="mascot" role="img" aria-label="Cartoon light bulb mascot wearing a green cap"></div>
    <div class="person">
      <p class="person-name">Dale Hartley</p>
      <p class="person-role">President</p>
    </div>
    <div class="contact">
      <p class="address">#22, 418 Maple Ridge Rd, St.Albert, Alberta.</p>
      <p class="contact-row">
        <svg viewBox="0 0 16 16" aria-hidden="true"><path d="M2 6 Q8 1 14 6 L12 8 L10 6 L6 6 L4 8 Z" fill="none" stroke="#8fd400" stroke-width="1.4"/><rect x="4" y="9" width="8" height="5" rx="1" fill="none" stroke="#8fd400" stroke-width="1.4"/></svg>
        <span>780-555-0138</span>
      </p>
      <p class="contact-row">
        <svg viewBox="0 0 16 16" aria-hidden="true"><rect x="1.5" y="3.5" width="13" height="9" fill="none" stroke="#8fd400" stroke-width="1.4"/><path d="M1.5 3.5 L8 9 L14.5 3.5" fill="none" stroke="#8fd400" stroke-width="1.4"/></svg>
        <span>support@vantorwiring.com</span>
      </p>
    </div>
    <div class="service-band">Commercial &amp; residential electrical repair and service</div>
  </section>
</main>
</body>
</html>
```